We are full service plumbing contractors that are capable of performing all of your plumbing need...

A clean, crisp website that conveys we can handle any plumbing from drain cleaning, repairs, to new construction. But emphasis on Leak detection, under-slab and underground water service leaks, repairs, and reroutes. Leak detection by acoustical, Thermal, or tracer gas , methods.Also emphasize advanced drain cleaning technologies and equipment. Don't just poke ahole in the drain blockage, Clean the pipe, with our High pressure hydrojetters, or Chain knocker drain cables that expand to the width of the pipe being cleaned.

Number of Pages Required

5+ page

Font styles to use
Sans Serif

Requirements
Should not have
• Canned photos

```html
<!DOCTYPE html>
<html lang="en">
<head>
<meta charset="utf-8">
<title>Tidal Pipeworks — Leak Detection &amp; Drain Cleaning</title>
<link rel="stylesheet" href="https://fonts.googleapis.com/css2?family=Mulish:wght@400;600;700&family=Montserrat:wght@600;700&display=swap">
<style>
:root{
  --ink:#1b1b1b;
  --text:#3d3d3d;
  --nav-blue:#1a70c0;
  --royal:#2b47a8;
  --accent:#2a4cb5;
  --link-blue:#1d6fd1;
  --panel:#e5e9f3;
  --panel-soft:#eef1f7;
  --band:#e6e8ea;
  --hero-light:#eff0f1;
  --btn-dark:#333333;
  --white:#ffffff;
}
*{box-sizing:border-box;margin:0;padding:0}
html,body{width:1200px;height:3742px;overflow:hidden;background:var(--white)}
body{position:relative;font-family:"Mulish",sans-serif;color:var(--text)}
.abs{position:absolute}
a{color:inherit;text-decoration:none}

/* header */
.topbar{left:0;top:0;width:1200px;height:92px;background:var(--white)}
.logo-box{left:92px;top:0;width:302px;height:150px;background:var(--white);z-index:3;display:flex;align-items:center;justify-content:center}
.logo-name{font-family:"Mulish",sans-serif;font-weight:700;font-size:30px;color:var(--royal)}
.emergency{left:620px;top:26px;display:flex;align-items:center;gap:14px;font-size:14px;line-height:20px;color:var(--ink)}
.btn-schedule{left:920px;top:27px;width:185px;height:43px;background:var(--btn-dark);color:var(--white);border-radius:5px;font-size:14px;font-weight:600;display:flex;align-items:center;justify-content:center}
.navbar{left:0;top:92px;width:1200px;height:53px;background:var(--nav-blue)}
.nav-links{left:484px;top:92px;height:53px;display:flex;align-items:center;font-size:15px;color:var(--white)}
.nav-links a{position:absolute;white-space:nowrap}

/* hero */
.hero{left:0;top:145px;width:1200px;height:531px;background:linear-gradient(90deg,#3a4b63 0%,#8d99a8 28%,#e4e7ea 42%,var(--hero-light) 100%)}
.hero-frame{left:622px;top:302px;width:228px;height:267px;border:3px solid var(--ink)}
.hero-kicker{left:678px;top:360px;font-family:"Montserrat",sans-serif;font-weight:600;font-size:22px;color:var(--ink)}
.hero-title{left:674px;top:392px;padding:0 4px;background:var(--hero-light);font-family:"Montserrat",sans-serif;font-weight:700;font-size:44px;line-height:54px;color:var(--ink);white-space:nowrap}
.btn-appoint{left:678px;top:459px;width:190px;height:43px;background:#111;color:var(--white);border-radius:5px;font-size:15px;display:flex;align-items:center;justify-content:center}

/* welcome */
.welcome-kicker{left:92px;top:836px;font-size:17px;color:var(--ink)}
.welcome-title{left:92px;top:862px;font-family:"Montserrat",sans-serif;font-weight:700;font-size:28px;color:var(--ink)}
.welcome-copy{left:92px;top:914px;width:405px;font-size:13.5px;line-height:22.5px;color:var(--text)}
.welcome-copy p+p{margin-top:22px}
.read-more{left:92px;top:1096px;font-size:15px;color:var(--ink);font-weight:600;border-bottom:2px solid var(--ink);padding-bottom:3px}
.photo{border-radius:2px}

/* help */
.help-kicker{left:137px;top:1262px;font-size:22px;color:var(--ink)}
.help-title{left:137px;top:1294px;font-family:"Montserrat",sans-serif;font-weight:700;font-size:32px;line-height:43px;color:var(--ink)}
.help-title .hl{color:var(--accent)}
.help-phone{left:137px;top:1386px;font-size:23px;color:var(--accent)}
.help-copy{left:559px;top:1282px;width:545px;font-size:16px;line-height:27px;color:var(--text)}
.btn-outline{border:2px solid var(--ink);border-radius:22px;color:var(--ink);font-size:14px;display:flex;align-items:center;justify-content:center;font-weight:600}
.btn-contact{left:559px;top:1380px;width:142px;height:40px}

/* experience */
.exp-band{left:267px;top:1529px;width:933px;height:544px;background:var(--panel)}
.exp-soft{left:0;top:1587px;width:407px;height:446px;background:var(--panel-soft);border-radius:0 14px 14px 0}
.exp-title{left:696px;top:1656px;font-family:"Montserrat",sans-serif;font-weight:700;font-size:30px;line-height:44px;color:var(--ink)}
.exp-list{left:696px;top:1803px;list-style:none;font-size:16px;color:var(--text)}
.exp-list li{display:flex;align-items:center;gap:14px;height:30px;white-space:nowrap}

/* services */
.services{left:0;top:2131px;width:1200px;height:589px;background:var(--royal)}
.services-title{left:0;top:2210px;width:1200px;text-align:center;font-size:26px;font-weight:400;color:var(--white)}
.btn-light{left:529px;top:2265px;width:145px;height:40px;border:2px solid var(--white);border-radius:22px;color:var(--white);font-size:15px;display:flex;align-items:center;justify-content:center}
.card-label{top:2622px;width:240px;text-align:center;font-size:15px;color:var(--white)}

/* projects */
.projects-title{left:916px;top:2898px;font-size:26px;font-weight:400;line-height:32px;color:var(--ink)}
.btn-view{left:918px;top:2979px;width:142px;height:40px}

/* emergency band */
.em-band{left:0;top:3189px;width:1200px;height:441px;background:var(--band)}
.em-line{left:492px;top:3333px;font-family:"Montserrat",sans-serif;font-weight:600;font-size:23px;line-height:35px;color:var(--ink)}
.em-sub{left:488px;top:3408px;font-weight:700;font-size:19px;color:var(--link-blue)}
.em-phone{left:492px;top:3453px;font-family:"Montserrat",sans-serif;font-weight:600;font-size:29px;color:var(--ink);border-bottom:3px solid var(--ink);padding-bottom:5px}

/* footer */
.footer-links{top:3670px;left:0;width:1200px;display:flex;justify-content:center;gap:30px;font-size:15px;color:var(--ink)}
.copyright{top:3700px;left:0;width:1200px;text-align:center;font-size:14px;color:var(--ink)}
</style>
</head>
<body>

<header>
  <div class="abs topbar"></div>
  <div class="abs logo-box"><span class="logo-name">Tidal Pipeworks</span></div>
  <div class="abs emergency">
    <svg width="26" height="26" viewBox="0 0 24 24" fill="none" stroke="#222" stroke-width="1.6"><path d="M5 3h4l2 5-2.5 1.5a11 11 0 0 0 6 6L16 13l5 2v4a2 2 0 0 1-2 2A16 16 0 0 1 3 5a2 2 0 0 1 2-2z"/></svg>
    <span>Got a Plumbing Emergency?<br>Call us now: 555.010.4161</span>
  </div>
  <a class="abs btn-schedule" href="#">Schedule a service</a>
  <div class="abs navbar"></div>
  <nav class="abs nav-links">
    <a style="left:0">Home</a>
    <a style="left:88px">About Us</a>
    <a style="left:205px">Services</a>
    <a style="left:315px">Project Gallery</a>
    <a style="left:476px">Contact Us</a>
  </nav>
</header>

<section>
  <div class="abs hero" role="img" aria-label="Plumber in a dark shirt wearing knee pads, fitting a chrome tap in a bright bathroom"></div>
  <div class="abs hero-frame"></div>
  <div class="abs hero-kicker">We are available for</div>
  <h1 class="abs hero-title">Plumbing Solutions</h1>
  <a class="abs btn-appoint" href="#">Get an appointment</a>
</section>

<section>
  <div class="abs welcome-kicker">Welcome to</div>
  <h2 class="abs welcome-title">Tidal Pipeworks Website</h2>
  <div class="abs welcome-copy">
    <p>We are full service plumbing contractors for homes and businesses, from drain cleaning and repairs to new construction. Our focus is hidden leaks: under-slab and underground water service leaks, repairs and reroutes.</p>
    <p>We find leaks by acoustic, thermal or tracer gas methods, and clean pipes wall to wall with hydrojetters and chain knocker cables.</p>
  </div>
  <a class="abs read-more" href="#">Read More</a>
  <div class="abs photo" style="left:566px;top:826px;width:260px;height:349px;background:linear-gradient(160deg,#6d6a62,#3e3a33 50%,#8f8a80)" role="img" aria-label="Excavated trench exposing a blue water service pipe in gravel"></div>
  <div class="abs photo" style="left:846px;top:781px;width:259px;height:349px;background:linear-gradient(170deg,#5f8a3a,#3d5a26 45%,#4a3426 75%,#6f9a45)" role="img" aria-label="Dug-out leak repair hole in a lawn with tools and a mat beside it"></div>
</section>

<section>
  <div class="abs help-kicker">We can help you !</div>
  <h2 class="abs help-title">FACING ANY<br><span class="hl">PLUMBING</span> PROBLEM?</h2>
  <div class="abs help-phone">call us on 1800-555-0142</div>
  <p class="abs help-copy">Hidden slab leak, failing water line or stubborn drain? We don't just poke a hole in the blockage: our hydrojetters and expanding chain knocker cables clean the whole pipe...</p>
  <a class="abs btn-outline btn-contact" href="#">Contact Us</a>
</section>

<section>
  <div class="abs exp-band"></div>
  <div class="abs exp-soft"></div>
  <div class="abs photo" style="left:115px;top:1637px;width:521px;height:339px;background:linear-gradient(180deg,#7b9a6a 0%,#a9b6a0 35%,#e9ecee 55%,#8a8c8e 80%,#6f7173)" role="img" aria-label="White service vans parked in a driveway under trees"></div>
  <h2 class="abs exp-title">Experienced Plumbers<br>Offering Quality Plumbing<br>Services</h2>
  <ul class="abs exp-list">
    <li><svg width="16" height="14" viewBox="0 0 16 14"><path d="M1 7l5 5L15 1" fill="none" stroke="#2a4cb5" stroke-width="2.4"/></svg>24 -Hours Emergency Services</li>
    <li><svg width="16" height="14" viewBox="0 0 16 14"><path d="M1 7l5 5L15 1" fill="none" stroke="#2a4cb5" stroke-width="2.4"/></svg>Acoustic, Thermal &amp; Tracer Gas Leak Detection</li>
    <li><svg width="16" height="14" viewBox="0 0 16 14"><path d="M1 7l5 5L15 1" fill="none" stroke="#2a4cb5" stroke-width="2.4"/></svg>High Pressure Hydrojetting</li>
    <li><svg width="16" height="14" viewBox="0 0 16 14"><path d="M1 7l5 5L15 1" fill="none" stroke="#2a4cb5" stroke-width="2.4"/></svg>Chain Knocker Pipe Cleaning</li>
    <li><svg width="16" height="14" viewBox="0 0 16 14"><path d="M1 7l5 5L15 1" fill="none" stroke="#2a4cb5" stroke-width="2.4"/></svg>Licensed, Insured, Free Estimates</li>
  </ul>
</section>

<section>
  <div class="abs services"></div>
  <h2 class="abs services-title">Leak Detection And Drain Cleaning Service</h2>
  <a class="abs btn-light" href="#">Read More</a>
  <div class="abs" style="left:92px;top:2358px;width:235px;height:249px;background:linear-gradient(150deg,#d8dde3,#8494a8 50%,#3c5d8c)" role="img" aria-label="Plumber repairing pipes under a sink"></div>
  <div class="abs" style="left:352px;top:2358px;width:237px;height:249px;background:linear-gradient(150deg,#9aa2aa,#5c6670 50%,#a43a2c)" role="img" aria-label="Red pipe wrench tightening a leaking fitting"></div>
  <div class="abs" style="left:614px;top:2358px;width:234px;height:249px;background:linear-gradient(150deg,#eef0f2,#c9ccd0 50%,#4f78b8)" role="img" aria-label="Plumber in a cap clearing a sink drain"></div>
  <div class="abs" style="left:873px;top:2358px;width:235px;height:249px;background:linear-gradient(150deg,#6e5a45,#3b8ad0 50%,#8a6c4e)" role="img" aria-label="Gloved hands joining a large blue water service pipe in a trench"></div>
  <div class="abs card-label" style="left:90px">Hydrojet Drain Cleaning</div>
  <div class="abs card-label" style="left:350px">Leak Detection &amp; Repairs</div>
  <div class="abs card-label" style="left:611px">Under-Slab Leaks</div>
  <div class="abs card-label" style="left:870px">Water Line Reroutes</div>
</section>

<section>
  <div class="abs" style="left:92px;top:2872px;width:237px;height:197px;background:linear-gradient(150deg,#5d7048,#3a3028 50%,#c8642a)" role="img" aria-label="Root-clogged drain pipe pulled into an orange bucket"></div>
  <div class="abs" style="left:352px;top:2872px;width:237px;height:197px;background:linear-gradient(160deg,#7a6a58,#3a2e24 50%,#6a5846)" role="img" aria-label="Open wall cavity showing an exposed water pipe"></div>
  <div class="abs" style="left:611px;top:2872px;width:237px;height:197px;background:linear-gradient(160deg,#bfb6a6,#6b4a32 50%,#a77a52)" role="img" aria-label="Rerouted copper water line beside a house wall"></div>
  <h2 class="abs projects-title">Our<br>latest projects</h2>
  <a class="abs btn-outline btn-view" href="#">View all</a>
</section>

<section>
  <div class="abs em-band"></div>
  <div class="abs" style="left:0;top:3189px;width:424px;height:441px;background:linear-gradient(135deg,#2d7fd6 0%,#5aa0e4 35%,#dfe3e6 60%,#e6e8ea 100%)" role="img" aria-label="Flat lay of faucet, hoses, fittings and washers on a blue and grey surface"></div>
  <p class="abs em-line">If you need any emergency plumbing service,<br>simply call our 24 hour emergency number</p>
  <p class="abs em-sub">Reliable Emergency Plumbing Service with Fair rates</p>
  <p class="abs em-phone">+(1800) 555 0187</p>
</section>

<footer>
  <nav class="abs footer-links">
    <a>Home</a><a>About Us</a><a>Services</a><a>Project Gallery</a><a>Contact Us</a>
  </nav>
  <p class="abs copyright">Copyright © Tidal Pipeworks 2019.All rights reserved</p>
</footer>

</body>
</html>
```